Simple Floral Service Web-Banner

I need to put a banner add on the members section of a website for an organization in which we are members.

The ad size is 470px x 214px.

I am uploading 4 pictures. 1 is a picture of red roses, and 1 is a picture of a t-shirt. These are 2 major products of ours which need to be incorporated in the banner. I do not have these in higher res or vectorized format, so please work with what you have. I am also uploading our 2 logos, one is for our Canadian company, and one for our American company. Both logos should be included at equal sizes.

The following text should be used:
"Proudly providing top quality roses, and custom commemorative grad t-shirts at over 800 schools."

I am just looking for a simple banner incorporating those pictures and that wording. I don't want something that is overly flashy.

I will monitor the submissions in a timely manner and give you feedback.

```html
<!DOCTYPE html>
<html lang="en">
<head>
<meta charset="utf-8">
<title>Capstone Blooms and Tassel Blooms Banner</title>
<link rel="stylesheet" href="https://fonts.googleapis.com/css2?family=PT+Sans:wght@700&display=swap">
<style>
  :root {
    --page: #ffffff;
    --frame-line: #c9c9c9;
    --panel-light: #f4f4f4;
    --panel-mid: #e0e0e0;
    --brand-green: #7cb342;
    --ink: #222222;
    --photo-border: #ffffff;
    --rose-red: #b3121c;
    --rose-deep: #6e0b10;
    --shirt-light: #ecebe8;
    --shirt-mid: #c9c8c4;
  }
  * { margin: 0; padding: 0; box-sizing: border-box; }
  html, body { width: 1200px; height: 545px; overflow: hidden; background: var(--page); }
  .banner {
    position: relative;
    width: 1200px;
    height: 545px;
    background: var(--page);
  }
  .banner-frame {
    position: absolute;
    left: 117px; top: 54px;
    width: 966px; height: 437px;
    border: 2px solid var(--frame-line);
    background: var(--page);
    padding: 8px;
  }
  .banner-panel {
    position: relative;
    width: 100%; height: 100%;
    background: radial-gradient(ellipse at 55% 45%, var(--panel-light) 0%, var(--panel-mid) 100%);
  }
  .brand {
    position: absolute;
    font-family: "PT Sans", sans-serif;
    font-weight: 700;
    color: var(--brand-green);
    font-size: 30px;
    line-height: 34px;
  }
  .brand-line { display: block; }
  .brand--canada { left: 27px; top: 18px; }
  .brand--canada .brand-line--second { padding-left: 40px; }
  .brand--usa { right: 27px; top: 18px; text-align: right; }
  .product-photo {
    position: absolute;
    border: 7px solid var(--photo-border);
    box-shadow: 0 2px 6px rgba(0,0,0,0.25);
  }
  .product-photo--roses {
    left: 235px; top: 19px;
    width: 194px; height: 224px;
    background: radial-gradient(ellipse at 45% 55%, var(--rose-red) 0%, var(--rose-deep) 55%, #f3eeea 100%);
  }
  .product-photo--shirts {
    left: 429px; top: 76px;
    width: 282px; height: 249px;
    transform: rotate(1.5deg);
    background: linear-gradient(160deg, var(--shirt-light) 0%, var(--shirt-mid) 100%);
  }
  .tagline {
    position: absolute;
    left: 0; right: 0; top: 337px;
    text-align: center;
    font-family: "PT Sans", sans-serif;
    font-weight: 700;
    font-size: 31px;
    line-height: 36px;
    color: var(--ink);
  }
</style>
</head>
<body>
<div class="banner">
  <div class="banner-frame">
    <div class="banner-panel">
      <div class="brand brand--canada">
        <span class="brand-line">Capstone</span>
        <span class="brand-line brand-line--second">Blooms</span>
      </div>
      <div class="product-photo product-photo--roses" role="img" aria-label="Bouquet of red roses with baby's breath"></div>
      <div class="product-photo product-photo--shirts" role="img" aria-label="Front and back of white commemorative graduation t-shirts"></div>
      <div class="brand brand--usa">
        <span class="brand-line">Tassel</span>
        <span class="brand-line">Blooms</span>
      </div>
      <p class="tagline">Proudly providing top quality&nbsp; roses, and custom commemorative<br>grad t-shirts at over 800 schools.</p>
    </div>
  </div>
</div>
</body>
</html>
```